Visitenkarten-Design für Fotograf gesucht
Zielgruppe
Ich bin Fotograf der ein step in Richtung Professionalität wagen möchte.
Aufgabenstellung
Ich habe bereits ein Logo welches ich als Datei angefügt habe.
Ich hatte überlegt gehabt eine Art Prägung im Design zu haben bzw. in der Visitenkarte, eventuell das Kamera Zeichen in meinem Logo. Sonst bin ich relativ offen.
Eine weitere Überlegung ist eine eher kontrastreiche Karte haben könnte, eventuell die Rückseite dunkelgrau oder schwarz.
Es kann wenn man eine dritte Farbe hinzufügen möchte ein mittleres bis dunkles Rot hinzufügen.
Ich habe ein paar Designs hinzugefügt die mir sehr zugesagt haben.
Ansonsten bin ich auch für ein Design in der kompletten Gegenteiligkeit offen.

```html
<!DOCTYPE html>
<html lang="de">
<head>
<meta charset="utf-8">
<title>Mirko Trell – Visitenkarte</title>
<link rel="stylesheet" href="https://fonts.googleapis.com/css2?family=Open+Sans:wght@400;600&display=swap">
<style>
  :root {
    --stage: #e4e2e0;
    --card-dark: #2f2a29;
    --card-light: #ffffff;
    --camera-grey: #57514f;
    --line-light: #bdb8b6;
    --text-dark: #2f2a29;
    --text-light: #f4f2f1;
    --accent-red: #b8262c;
  }
  * { box-sizing: border-box; margin: 0; padding: 0; }
  html, body {
    width: 1200px; height: 800px; overflow: hidden;
    background: var(--stage);
    font-family: "Open Sans", Arial, sans-serif;
  }
  .stage {
    width: 1200px; height: 800px;
    display: flex; align-items: center; justify-content: center; gap: 60px;
  }
  .card {
    position: relative; width: 520px; height: 306px; overflow: hidden;
    box-shadow: 0 10px 30px rgba(0,0,0,.18);
  }
  /* Front side */
  .card-front { background: var(--card-light); }
  .front-header {
    position: absolute; left: 0; top: 0; width: 100%; height: 158px;
    background: var(--card-dark);
  }
  .front-header .camera-art {
    position: absolute; left: 238px; top: 8px; width: 110px; height: 150px;
  }
  .front-header .rule {
    position: absolute; left: 0; top: 128px; width: 100%; height: 1px;
    background: var(--line-light);
  }
  .wordmark {
    position: absolute; display: flex; align-items: center; gap: 10px;
    color: var(--text-light); font-weight: 400; letter-spacing: .02em;
    white-space: nowrap;
  }
  .wordmark .mark-square {
    width: 14px; height: 14px; border: 1.5px solid var(--text-light);
  }
  .front-header .wordmark { left: 150px; top: 72px; font-size: 34px; }
  .contact {
    position: absolute; left: 110px; top: 178px; width: 300px;
    font-size: 15px; line-height: 1.45; color: var(--text-dark);
    text-align: center; font-style: normal; white-space: nowrap;
  }
  .contact .dot { color: var(--accent-red); padding: 0 4px; }
  .front-band {
    position: absolute; left: 0; top: 272px; width: 100%; height: 1px;
    background: var(--text-dark);
  }
  .front-band.short { left: 410px; width: 90px; top: 184px; }
  /* Back side */
  .card-back { background: var(--card-dark); }
  .card-back .camera-art {
    position: absolute; right: 0; top: 0; width: 205px; height: 100%;
  }
  .card-back .wordmark { left: 34px; bottom: 52px; font-size: 36px; }
</style>
</head>
<body>
<main class="stage">
  <section class="card card-front" aria-label="Vorderseite">
    <div class="front-header">
      <svg class="camera-art" role="img" aria-label="Dezente Illustration einer zweiäugigen Spiegelreflexkamera" viewBox="0 0 110 150">
        <rect width="110" height="150" fill="var(--camera-grey)" opacity=".55"/>
      </svg>
      <div class="rule"></div>
      <div class="wordmark"><span>Mirko Trell</span><span class="mark-square"></span></div>
    </div>
    <div class="front-band short"></div>
    <address class="contact">
      birkenallee 17<span class="dot">•</span>53119 feldhausen<br>
      +49 211 380 442<span class="dot">•</span>+49 157 220 918<br>
      info@mt-photography.de<br>
      www.mt-photography.de
    </address>
    <div class="front-band"></div>
  </section>

  <section class="card card-back" aria-label="Rückseite">
    <svg class="camera-art" role="img" aria-label="Große Illustration einer zweiäugigen Kamera im Anschnitt" viewBox="0 0 205 306" preserveAspectRatio="none">
      <defs>
        <linearGradient id="cameraTone" x1="0" x2="1" y1="0" y2="0">
          <stop offset="0" stop-color="#4a4442"/>
          <stop offset="1" stop-color="#5f5957"/>
        </linearGradient>
      </defs>
      <rect width="205" height="306" fill="url(#cameraTone)"/>
    </svg>
    <div class="wordmark"><span>Mirko Trell</span><span class="mark-square"></span></div>
  </section>
</main>
</body>
</html>
```